High quality health product needs a label

If you are a top professional designer for exclusive product labels, please read on.

High quality health products are being filled into so called Talvo glass bottles (see attachment) and I want to create labels for a range of different herbs (i.e. teasel, artemesia annua) in various dosage forms (i.e. liquid, capsules and tea). The brand of these products is called quellona.

The label for each type of herb shall have a small variance in color, i.e. teasel can have some violet and artemesia annua a green theme. The variance in color should be unique (not just 2 circles and a triangle) and abstract (i.e. no leafs). Please have a look at 2 of our labels we have created for other products.

The logo I feel comfortable with is attached in the file pixelgrove. I only want to take the leaf as logo, nothing else. The color of the logo should be adapted to our needs, but a green leaf makes sense to me. The color of the logo does not change for the variations of the label.

What do I expect in terms of design:

- minimalistic
- exclusive
- luxury
- classy
- abstract
- playful
- uniqueness

The front of the label should show:
- logo
- name of the herb, i.e. teasel
- dosage form, i.e. extract
- content, i.e. 250 ml
- the 2 logos to indicate that the product is certified organic

The back will contain some basic information that I will provide once I selected your design.

The final deliverables are 4 illustrator (compatible with version 16) ai vector files for 4 different types of herbs. Once the initial design is set, we need to create 3 color variations.

Please use a 100 mm x 210 mm layout for the 500 ml syrup bottle.

Target Market(s)

people with an interest in their health

Industry/Entity Type

health

Font styles to use
Sans Serif

Requirements
Must have
• abstract, unique, luxury, high class, minimalistic
Should not have
• overloaded, too many colors,

```html
<!DOCTYPE html>
<html lang="en">
<head>
<meta charset="UTF-8">
<title>Quellona Extract Labels</title>
<link rel="stylesheet" href="https://fonts.googleapis.com/css2?family=Abril+Fatface&family=Poppins:wght@300;400;600&display=swap">
<style>
  :root {
    --page-bg: #ffffff;
    --gold: #d9c798;
    --gold-soft: #cbb98a;
    --brand-green: #3f6b1e;
    --green-light: #5f8644;
    --green-mid: #2c5212;
    --green-dark: #3b5f22;
    --green-band: #46663a;
    --green-deep: #1d3d1c;
    --violet-light: #9c5cb4;
    --violet-mid: #7a2c98;
    --violet-dark: #5e167c;
    --violet-band: #7a3e92;
    --violet-deep: #5b1a78;
    --badge-green: #2f6b2a;
    --badge-light: #e8eae4;
  }
  * { margin: 0; padding: 0; box-sizing: border-box; }
  html, body { width: 1200px; height: 900px; overflow: hidden; background: var(--page-bg); }
  .stage {
    position: relative; width: 1200px; height: 900px;
    display: flex; justify-content: center; align-items: center; gap: 80px;
  }
  .label {
    position: relative; width: 430px; height: 580px; overflow: hidden;
    font-family: "Poppins", sans-serif;
  }
  .label--artemisia {
    --label-bg: linear-gradient(90deg, var(--green-mid) 0%, var(--green-light) 22%, var(--green-mid) 48%, var(--green-dark) 80%, var(--green-mid) 100%);
    --band: var(--green-band);
    --deep: var(--green-deep);
    --pill-text: var(--green-mid);
  }
  .label--teasel {
    --label-bg: linear-gradient(90deg, var(--violet-mid) 0%, var(--violet-light) 22%, var(--violet-mid) 48%, var(--violet-dark) 85%, var(--violet-mid) 100%);
    --band: var(--violet-band);
    --deep: var(--violet-deep);
    --pill-text: var(--violet-mid);
  }
  .label__surface { position: absolute; inset: 0; background: var(--label-bg); }
  .label__waves { position: absolute; left: 0; bottom: 0; width: 430px; height: 240px; }
  .label__waves .wave-band { fill: var(--band); opacity: 0.55; }
  .label__waves .wave-deep { fill: var(--deep); opacity: 0.6; }

  .brand {
    position: absolute; top: 74px; left: 0; right: 0;
    display: flex; justify-content: center; align-items: center; gap: 7px;
    color: var(--gold); font-weight: 600; font-size: 17px; letter-spacing: 0.06em;
  }
  .brand__dot { width: 10px; height: 10px; border-radius: 50%; background: var(--brand-green); }

  .product {
    position: absolute; right: 73px; text-align: right; color: var(--gold);
  }
  .product__tag { font-weight: 300; font-size: 13px; letter-spacing: 0.02em; line-height: 1; }
  .product__name {
    font-family: "Abril Fatface", serif; font-weight: 400; line-height: 0.82;
    letter-spacing: -0.01em;
  }
  .label--artemisia .product { top: 196px; }
  .label--artemisia .product__name { font-size: 54px; margin-top: 6px; }
  .label--teasel .product { top: 199px; }
  .label--teasel .product__name { font-size: 86px; margin-top: 4px; }
  .product__form { font-weight: 300; font-size: 13px; line-height: 1; margin-top: 4px; }

  .dosage {
    position: absolute; top: 410px; left: 50%; transform: translateX(-50%);
    background: var(--gold); color: var(--pill-text);
    font-size: 27px; font-weight: 400; line-height: 44px; height: 44px;
    padding: 0 16px; border-radius: 4px;
  }

  .meta {
    position: absolute; bottom: 48px; color: var(--gold);
  }
  .meta__title { font-weight: 300; font-size: 13px; line-height: 1; }
  .meta--content { left: 40px; }
  .meta__value { font-weight: 400; font-size: 26px; line-height: 1; margin-top: 9px; letter-spacing: -0.01em; }
  .meta--certified { right: 40px; text-align: right; }
  .cert-badges { display: flex; justify-content: flex-end; gap: 8px; margin-top: 10px; align-items: center; }
  .cert-badge--round { width: 20px; height: 20px; border-radius: 50%; background: var(--badge-light); }
  .cert-badge--leaf { width: 32px; height: 20px; background: var(--badge-green); }
</style>
</head>
<body>
<main class="stage">
  <article class="label label--artemisia">
    <div class="label__surface"></div>
    <svg class="label__waves" viewBox="0 0 430 240" preserveAspectRatio="none" aria-hidden="true">
      <path class="wave-band" d="M0 0 Q215 110 430 20 L430 240 L0 240 Z"/>
      <path class="wave-deep" d="M0 40 Q215 150 430 40 L430 240 L0 240 Z"/>
    </svg>
    <div class="brand"><span class="brand__dot"></span>QUELLONA</div>
    <div class="product">
      <p class="product__tag">PREMIUM QUALITY</p>
      <h2 class="product__name">artemesia<br>annua</h2>
      <p class="product__form">EXTRACT</p>
    </div>
    <div class="dosage">liquid</div>
    <div class="meta meta--content">
      <p class="meta__title">Net content:</p>
      <p class="meta__value">250ml</p>
    </div>
    <div class="meta meta--certified">
      <p class="meta__title">Certified by:</p>
      <div class="cert-badges">
        <span class="cert-badge cert-badge--round"></span>
        <span class="cert-badge cert-badge--leaf"></span>
      </div>
    </div>
  </article>

  <article class="label label--teasel">
    <div class="label__surface"></div>
    <svg class="label__waves" viewBox="0 0 430 240" preserveAspectRatio="none" aria-hidden="true">
      <path class="wave-band" d="M0 0 Q215 110 430 20 L430 240 L0 240 Z"/>
      <path class="wave-deep" d="M0 40 Q215 150 430 40 L430 240 L0 240 Z"/>
    </svg>
    <div class="brand"><span class="brand__dot"></span>QUELLONA</div>
    <div class="product">
      <p class="product__tag">PREMIUM QUALITY</p>
      <h2 class="product__name">teasel</h2>
      <p class="product__form">EXTRACT</p>
    </div>
    <div class="dosage">liquid</div>
    <div class="meta meta--content">
      <p class="meta__title">Net content:</p>
      <p class="meta__value">250ml</p>
    </div>
    <div class="meta meta--certified">
      <p class="meta__title">Certified by:</p>
      <div class="cert-badges">
        <span class="cert-badge cert-badge--round"></span>
        <span class="cert-badge cert-badge--leaf"></span>
      </div>
    </div>
  </article>
</main>
</body>
</html>
```